詳細はzipファイルにまとめておりおますので、こちらからダウンロードしてください。

http://3.hakobuya.nu/0522-k83920fa17de462093b8e1c7f06a35d9

【デザインの参考サイト】
クライアント様からは、以下の参考サイトを挙げていただいております。
http://plumtivra.com/
https://sorvik4417.com/

ただし、上記サイトはおしゃれではあるものの、少しアピールが弱いようにも思います。
最終的な成果(査定依頼や、来店予約)に結びつきやすいような工夫があれば嬉しいです。

【継続発注について】
まずはトップページのみのデザインをお願い致します。
トップページのデザインが決まりましたら、下層ページのデザインもお願いする予定です。(1ページ1~2万円程度の予定)
下層ページは2~3ページほどの予定ですので、総額12万円ぐらいの予定です。

【スマホ対応について】
コーディング時に、レスポンシブ対応する予定ですので、スマホ対応しやすいデザインにしていただければ助かります。

【レイアウトの変更などについて】
基本的にはワイヤーに沿って作っていただければと思います。
ただし、「もっとこうしたほうが良いのでは?」「こんな形はどうか?」といったようなご提案があれば、別途ご相談ください。

必要な資料は上記のzipファイルの中に入れておりますので、そちらをご覧ください。
もし不明な点があれば遠慮なくご連絡くださいませ。
1ページ
シンプル 複雑
単色 カラフル
暗い 明るい
日常 高級
遊び心 厳粛
未来的 伝統的
女性的 男性的
黄・オレンジ系
• 高解像度JPG (.jpg)
• イラストレーター形式 (.ai)
納品は、IllustratorでもPhotoshopでもFireworksでも、どのファイルでもOKです。

また、納品の際には使っているフォントをお教えください。
(使用フォントはモリサワ、もしくはフリーフォントでお願いします)
たくさんのご応募ありがとうございました。
非常に悩んだのですが、お一人の方を選ばせていただきました。
選に漏れた方々につきましては、お手数おかけしたにも関わらず何もお返しできずに心苦しくもあるのですが、ご了承いただければ幸いです。
またこれに懲りず、今後ともよろしくお願いいたします。
ありがとうございました!

いいデザインをしていただいた方が数人おられて、非常に悩みました。
その中で一番こちらの意図を汲み取っていただき、バランスの取れたデザインをしていただいた、ということで、こちらの方にお願いすることにしました。

たくさんのご応募ありがとうございました。
ありがとうございました!

```html
<!DOCTYPE html>
<html lang="ja">
<head>
<meta charset="utf-8">
<title>タカネ｜7階以上の高層階限定 マンション買取サービス</title>
<link rel="stylesheet" href="https://fonts.googleapis.com/css2?family=Noto+Sans+JP:wght@400;500;700;900&display=swap">
<style>
:root{
  --orange:#f39a1e;
  --orange-deep:#e8850c;
  --orange-soft:#fdf1e2;
  --pink-soft:#fdf3ef;
  --ink:#333;
  --ink-soft:#666;
  --line:#ddd;
  --gray-band:#ececec;
  --white:#fff;
}
*{box-sizing:border-box;margin:0;padding:0}
html,body{width:1200px;height:3776px;overflow:hidden}
body{font-family:"Noto Sans JP",sans-serif;color:var(--ink);background:var(--white);font-size:13px;line-height:1.7}
.inner{width:880px;margin:0 auto;position:relative}

.site-header{height:48px;background:var(--white);border-bottom:1px solid var(--line)}
.site-header .inner{width:1040px;height:48px;display:flex;align-items:center}
.brand{display:flex;align-items:center;gap:10px}
.brand-name{font-weight:900;font-size:24px;letter-spacing:2px;color:var(--ink)}
.brand-tag{font-size:10px;line-height:1.3;color:var(--ink-soft);margin-left:6px}
.global-nav{margin-left:auto;display:flex;height:100%;align-items:flex-end}
.global-nav a{font-size:11px;color:var(--ink);text-decoration:none;padding:0 14px 8px;border-left:1px solid var(--line)}
.reserve-btn{position:absolute;right:0;top:0;background:var(--orange);color:#fff;font-size:11px;font-weight:700;padding:3px 18px;text-decoration:none}

.hero{height:512px;position:relative;background:linear-gradient(180deg,#7aa7d2 0%,#a9c4dd 40%,#8a96a3 70%,#5f6b77 100%)}
.hero-title{position:absolute;left:0;right:0;top:270px;text-align:center;color:#fff;font-size:44px;font-weight:700;letter-spacing:3px;text-shadow:0 2px 6px rgba(0,0,0,.35)}

.intro{height:160px}
.intro .inner{display:flex;padding-top:30px}
.intro-text{flex:1;font-size:12.5px;line-height:1.9}
.intro-map{width:200px;height:110px;background:#eef0f2;border-radius:4px;margin-left:30px}

.features{height:360px}
.features .inner{display:flex;gap:20px}
.feature{flex:1}
.feature-head{border:1px solid var(--line);border-bottom:none;text-align:center;font-weight:700;font-size:14px;padding:12px 0 4px;background:#fff}
.feature-icon{height:130px;border:1px solid var(--line);border-top:none;border-bottom:none;display:flex;justify-content:center;align-items:center}
.feature-icon span{display:block;width:110px;height:100px;background:#d9d9d9;border-radius:6px}
.feature-band{height:34px;background:var(--orange)}
.feature p{font-size:11.5px;line-height:1.8;margin-top:14px;color:var(--ink-soft)}

.btn-band{background:var(--gray-band);display:flex;align-items:center;justify-content:center;height:110px}
.outline-btn{display:inline-block;width:260px;text-align:center;background:#fff;border:1px solid #bbb;padding:10px 0;font-size:15px;font-weight:700;color:var(--ink);text-decoration:none;position:relative}
.outline-btn::before{content:"";position:absolute;left:18px;top:50%;width:14px;height:14px;margin-top:-7px;background:var(--orange);border-radius:50%}

.section-title{display:flex;align-items:center;justify-content:center;gap:12px;height:50px;border:2px solid var(--orange);background:#fff;font-size:20px;font-weight:700}
.section-title i{width:22px;height:22px;background:var(--orange);border-radius:3px}

.compare{height:560px;padding-top:40px}
.compare-cols{display:flex;gap:60px;margin-top:30px}
.compare-col{flex:1;text-align:center}
.compare-col h3{font-size:24px;font-weight:900;margin-bottom:12px}
.compare-illust{width:250px;height:250px;border-radius:50%;margin:0 auto}
.compare-col.site .compare-illust{background:#e2e2e2}
.compare-col.ours .compare-illust{background:var(--orange)}
.compare-col p{text-align:left;font-size:11.5px;line-height:1.8;margin-top:26px;color:var(--ink-soft)}

.faq{height:700px;padding-top:20px}
.faq-box{background:var(--orange-soft);padding:20px 20px 0;height:660px}
.faq-list{margin-top:20px}
.qa{margin-bottom:8px}
.qa-row{display:flex;align-items:stretch}
.qa-mark{width:40px;flex:none;display:flex;align-items:center;justify-content:center;color:#fff;font-weight:900;font-size:20px}
.qa-q .qa-mark{background:#b5b5b5}
.qa-a .qa-mark{background:var(--orange)}
.qa-text{flex:1;padding:6px 12px;font-size:11px;line-height:1.7}
.qa-q .qa-text{background:#fff;font-weight:700;height:44px}
.qa-a .qa-text{background:var(--pink-soft);color:var(--ink-soft);height:54px}

.results{height:620px;padding-top:30px}
.result{display:flex;gap:20px;margin-top:30px;height:240px}
.result-photo{width:190px;height:230px;background:linear-gradient(180deg,#b9cde0,#8d9eae)}
.result-body{flex:1}
.result-name{background:var(--orange);color:#fff;font-weight:700;font-size:14px;padding:4px 12px}
.result-table{width:100%;border-collapse:collapse;margin-top:8px;font-size:11px}
.result-table th,.result-table td{border-bottom:1px solid var(--line);padding:4px 8px;text-align:left}
.result-table th{width:90px;background:#f6f6f6;font-weight:500}
.result-side{width:300px}
.result-side p{font-size:11px;line-height:1.8;color:var(--ink-soft)}
.detail-btn{display:block;width:110px;margin:0 0 10px auto;background:var(--orange);color:#fff;text-align:center;font-size:11px;font-weight:700;padding:3px 0;text-decoration:none}

.banners{height:290px}
.banners .inner{display:flex;gap:40px;padding-top:30px}
.banner{flex:1;height:230px;display:flex;align-items:flex-end;justify-content:center;padding-bottom:28px;text-decoration:none;border:3px solid var(--orange)}
.banner.assess{background:linear-gradient(180deg,#d7e6f3,#a7c0d7)}
.banner.visit{background:linear-gradient(180deg,#f7f3ee,#e6ddd2)}
.banner span{background:rgba(255,255,255,.92);color:var(--orange-deep);font-size:24px;font-weight:900;padding:6px 22px;border-radius:4px}

.site-footer{height:270px;background:#f4f2ef;border-top:4px solid var(--orange)}
.site-footer .inner{display:flex;padding-top:40px;width:1000px}
.footer-info{width:360px}
.footer-info .brand-name{font-size:30px}
.footer-info address{font-style:normal;font-size:11px;line-height:1.8;margin-top:14px;color:var(--ink-soft)}
.footer-tel{font-size:22px;font-weight:700;margin-top:6px;display:flex;align-items:center;gap:8px}
.footer-about{width:300px;font-size:11px;line-height:1.8;color:var(--ink-soft);padding:0 20px}
.footer-nav{flex:1;display:grid;grid-template-columns:1fr 1fr 1fr;gap:6px 10px;font-size:11px;align-content:start}
.footer-nav a{color:var(--ink);text-decoration:none;white-space:nowrap}
.footer-nav a::before{content:"› ";color:var(--orange)}
.copyright{height:36px;background:var(--orange);color:#fff;font-size:10px;display:flex;align-items:center;justify-content:center;position:relative}
.page-top{position:absolute;right:20px;top:-50px;width:40px;height:40px;background:var(--orange);display:flex;align-items:center;justify-content:center}
</style>
</head>
<body>

<header class="site-header">
  <div class="inner">
    <div class="brand">
      <span class="brand-name">タカネ</span>
      <span class="brand-tag">7階以上の高層階限定<br>マンション買取サービス</span>
    </div>
    <nav class="global-nav">
      <a href="#">タカネとは</a>
      <a href="#">買取について</a>
      <a href="#">買取の流れ</a>
      <a href="#">無料査定申込</a>
    </nav>
    <a class="reserve-btn" href="#">ご来店予約</a>
  </div>
</header>

<section class="hero" role="img" aria-label="高層マンションが立ち並ぶ都市の街並みと青空の写真">
  <h1 class="hero-title">7階以上のお部屋、買い取ります。</h1>
</section>

<section class="intro">
  <div class="inner">
    <p class="intro-text">
      「タカネ」は、7階以上の高層階限定のマンション買取サービスです。<br>
      高層階ならではの眺望や住み心地を正しく評価し、適正な価格でお買い取りいたします。<br>
      「タカネ」が、あなたの大切なお部屋の売却をしっかりとサポートします。
    </p>
    <div class="intro-map" role="img" aria-label="対応エリアを示す地域の地図"></div>
  </div>
</section>

<section class="features">
  <div class="inner">
    <div class="feature">
      <div class="feature-head">納得の金額をご提示します!</div>
      <div class="feature-icon"><span role="img" aria-label="貯金箱のイラスト"></span></div>
      <div class="feature-band"></div>
      <p>高層階マンションの価値を正しく見極め、相場をふまえた納得の金額をご提示いたします。査定後のご相談もお気軽にどうぞ。</p>
    </div>
    <div class="feature">
      <div class="feature-head">査定もスムーズ!すばやく現金化できます</div>
      <div class="feature-icon"><span role="img" aria-label="握手のイラスト"></span></div>
      <div class="feature-band"></div>
      <p>ご依頼から査定、お引き渡しまでスムーズに進めます。お急ぎの方にもすばやく対応いたします。</p>
    </div>
    <div class="feature">
      <div class="feature-head">査定は無料!仲介手数料もかかりません</div>
      <div class="feature-icon"><span role="img" aria-label="チェックリストのイラスト"></span></div>
      <div class="feature-band"></div>
      <p>査定は完全無料です。直接買取のため、仲介手数料などの余計な費用は一切かかりません。</p>
    </div>
  </div>
</section>

<div class="btn-band"><a class="outline-btn" href="#">タカネについて</a></div>

<section class="compare">
  <div class="inner">
    <h2 class="section-title"><i></i>一括見積りサイトとの違い</h2>
    <div class="compare-cols">
      <div class="compare-col site">
        <h3>一括見積りサイト</h3>
        <div class="compare-illust" role="img" aria-label="多くの業者から連絡が集中して困る人のイラスト"></div>
        <p>個人情報が多くの会社に送られてしまうため、電話やメールが一度に集中し、対応に追われることがあります。<br>金額の比較はできても、手間や時間が多くかかる場合があります。</p>
      </div>
      <div class="compare-col ours">
        <h3>タカネ</h3>
        <div class="compare-illust" role="img" aria-label="マンションから家族へ直接つながる流れのイラスト"></div>
        <p>直接の買取なので、情報が他社へ渡ることはありません。<br>・高層階の価値を専門に評価し、適正な金額を提示<br>・やり取りは一社のみで、手間や時間を大幅に削減<br>・仲介手数料は不要です</p>
      </div>
    </div>
  </div>
</section>

<section class="faq">
  <div class="inner">
    <div class="faq-box">
      <h2 class="section-title"><i></i>よくあるご質問</h2>
      <div class="faq-list">
        <div class="qa">
          <div class="qa-row qa-q"><span class="qa-mark">Q</span><p class="qa-text">査定を依頼したら必ず売却しなければいけませんか?<br>査定額を見てから検討したいのですが大丈夫でしょうか。</p></div>
          <div class="qa-row qa-a"><span class="qa-mark">A</span><p class="qa-text">ご安心ください。査定後に売却をお断りいただいても問題ありません。<br>金額をご確認のうえ、ゆっくりご検討ください。費用も一切かかりません。</p></div>
        </div>
        <div class="qa">
          <div class="qa-row qa-q"><span class="qa-mark">Q</span><p class="qa-text">住宅ローンが残っていても買取は可能ですか?<br>残債の状況によって対応は変わりますか。</p></div>
          <div class="qa-row qa-a"><span class="qa-mark">A</span><p class="qa-text">ローンが残っている場合でもお買い取りは可能です。<br>残債の精算方法も含めて、担当者が丁寧にご案内いたします。</p></div>
        </div>
        <div class="qa">
          <div class="qa-row qa-q"><span class="qa-mark">Q</span><p class="qa-text">入居者がいる状態でも売却できますか?<br>賃貸中の物件についても教えてください。</p></div>
          <div class="qa-row qa-a"><span class="qa-mark">A</span><p class="qa-text">賃貸中のお部屋もそのままお買い取りできます。<br>入居者様への対応についてもご相談ください。</p></div>
        </div>
        <div class="qa">
          <div class="qa-row qa-q"><span class="qa-mark">Q</span><p class="qa-text">査定から現金化まで、どのくらいの期間がかかりますか?<br>急ぎで売却したい場合はどうすればよいですか。</p></div>
          <div class="qa-row qa-a"><span class="qa-mark">A</span><p class="qa-text">最短で数日での現金化が可能です。<br>お急ぎの場合はお申し込み時にその旨をお伝えください。</p></div>
        </div>
        <div class="qa">
          <div class="qa-row qa-q"><span class="qa-mark">Q</span><p class="qa-text">室内が古くてもリフォームは必要ですか?<br>荷物が残っている場合の対応も知りたいです。</p></div>
          <div class="qa-row qa-a"><span class="qa-mark">A</span><p class="qa-text">リフォームの必要はありません。現状のままお買い取りいたします。<br>残された家具や荷物の処分についてもご相談ください。</p></div>
        </div>
      </div>
    </div>
  </div>
</section>

<section class="results">
  <div class="inner">
    <h2 class="section-title"><i></i>買取実績</h2>
    <article class="result">
      <div class="result-photo" role="img" aria-label="高層マンションの外観写真"></div>
      <div class="result-body">
        <div class="result-name">大阪マンション</div>
        <table class="result-table">
          <tr><th>所在地</th><td>大阪市北区</td></tr>
          <tr><th>階数</th><td>12階</td></tr>
          <tr><th>間取り</th><td>3LDK</td></tr>
          <tr><th>築年数</th><td>15年</td></tr>
          <tr><th>買取期間</th><td>2週間</td></tr>
        </table>
      </div>
      <div class="result-side">
        <a class="detail-btn" href="#">詳細を見る</a>
        <p>眺望の良い高層階のお部屋を、ご相談から約2週間でお買い取りしました。住み替えのご予定に合わせて、お引き渡しの日程を柔軟に調整いたしました。</p>
      </div>
    </article>
    <article class="result">
      <div class="result-photo" role="img" aria-label="高層マンションの外観写真"></div>
      <div class="result-body">
        <div class="result-name">大阪マンション</div>
        <table class="result-table">
          <tr><th>所在地</th><td>大阪市中央区</td></tr>
          <tr><th>階数</th><td>9階</td></tr>
          <tr><th>間取り</th><td>2LDK</td></tr>
          <tr><th>築年数</th><td>20年</td></tr>
          <tr><th>買取期間</th><td>10日</td></tr>
        </table>
      </div>
      <div class="result-side">
        <a class="detail-btn" href="#">詳細を見る</a>
        <p>相続されたお部屋のご相談でした。室内の荷物が残ったままの状態でしたが、現状のままでお買い取りし、スムーズに現金化いたしました。</p>
      </div>
    </article>
  </div>
</section>

<div class="btn-band"><a class="outline-btn" href="#">買取実績をもっと見る</a></div>

<section class="banners">
  <div class="inner">
    <a class="banner assess" href="#" role="img" aria-label="家族が住むマンションの写真に無料査定の案内"><span>買取相談はこちら</span></a>
    <a class="banner visit" href="#" role="img" aria-label="受付スタッフの写真にご来店予約の案内"><span>ご来店予約はこちら</span></a>
  </div>
</section>

<footer class="site-footer">
  <div class="inner">
    <div class="footer-info">
      <div class="brand"><span class="brand-name">タカネ</span><span class="brand-tag">7階以上の高層階限定<br>マンション買取サービス</span></div>
      <address>運営：株式会社タカネリビング<br>〒530-0000 大阪府大阪市北区中央1-2-3 タカネビル5F</address>
      <div class="footer-tel">
        <svg width="20" height="20" viewBox="0 0 24 24"><path fill="#f39a1e" d="M6.6 10.8a15 15 0 0 0 6.6 6.6l2.2-2.2c.3-.3.7-.4 1-.2 1.1.4 2.3.6 3.6.6.6 0 1 .4 1 1V20c0 .6-.4 1-1 1A17 17 0 0 1 3 4c0-.6.4-1 1-1h3.5c.6 0 1 .4 1 1 0 1.3.2 2.5.6 3.6.1.3 0 .7-.2 1z"/></svg>
        06-0000-4821
      </div>
    </div>
    <p class="footer-about">タカネは、7階以上の高層階マンションに特化した買取サービスです。眺望や日当たりなど高層階ならではの価値を正しく評価し、適正価格でのお買い取りを行っております。</p>
    <nav class="footer-nav">
      <a href="#">タカネとは</a><a href="#">買取について</a><a href="#">買取の流れ</a>
      <a href="#">買取実績</a><a href="#">よくある質問</a><a href="#">無料査定申込</a>
      <a href="#">ご来店予約</a><a href="#">会社概要</a><a href="#">個人情報保護</a>
    </nav>
  </div>
</footer>
<div class="copyright">
  Copyright © Takane Living Co., Ltd. All Rights Reserved.
  <a class="page-top" href="#" aria-label="ページ上部へ"><svg width="18" height="18" viewBox="0 0 24 24"><path d="M12 6l-7 8h14z" fill="#fff"/></svg></a>
</div>

</body>
</html>
```